Company business card

We need a new business card design. We are IT company which is specialized for outsourcing of operations hardware and software (specially Quorvane, we are a partner), developing custom applications and web applications, BPM solutions, auditing hw and sw. actually design was attached. But we need completely NEW.

Business

```html
<!DOCTYPE html>
<html lang="sk">
<head>
<meta charset="utf-8">
<title>KAVREL – business card</title>
<link rel="stylesheet" href="https://fonts.googleapis.com/css2?family=Montserrat:wght@600;700&family=Source+Sans+3:wght@400&display=swap">
<style>
  :root {
    --backdrop: #a9a7a8;
    --brand-blue: #3a69ab;
    --brand-blue-deep: #2f5a98;
    --swoosh-grey: #7a7a7c;
    --paper: #fbfbfb;
    --ink-grey: #6a6a6a;
    --white: #ffffff;
  }
  * { margin: 0; padding: 0; box-sizing: border-box; }
  html, body { width: 1200px; height: 1200px; overflow: hidden; }
  body {
    background: var(--backdrop);
    position: relative;
    font-family: "Montserrat", sans-serif;
  }
  .card {
    position: absolute;
    width: 712px;
    height: 417px;
    border-radius: 20px;
    overflow: hidden;
  }
  .card-front {
    left: 238px; top: 118px;
    background: var(--brand-blue);
  }
  .card-front .binary-field {
    position: absolute; inset: 0;
    background: linear-gradient(135deg, var(--brand-blue) 0%, var(--brand-blue-deep) 100%);
  }
  .wordmark {
    position: absolute;
    display: flex;
    align-items: center;
  }
  .wordmark-square { flex: none; }
  .wordmark-name {
    font-family: "Montserrat", sans-serif;
    font-weight: 700;
    line-height: 0.9;
    letter-spacing: -1px;
  }
  .card-front .wordmark { left: 177px; top: 137px; gap: 30px; }
  .card-front .wordmark-square { width: 146px; height: 146px; background: var(--white); }
  .card-front .wordmark-name { color: var(--white); font-size: 80px; }

  .card-back {
    left: 230px; top: 645px;
    background: var(--paper);
  }
  .card-back .header-wave { position: absolute; left: 0; top: 0; }
  .company-name {
    position: absolute;
    right: 49px; top: 50px;
    text-align: right;
    color: var(--white);
    font-weight: 600;
    font-size: 27px;
    line-height: 40px;
    letter-spacing: 1px;
  }
  .holder { position: absolute; left: 44px; top: 118px; }
  .holder-name { color: var(--brand-blue); font-weight: 600; font-size: 28px; letter-spacing: 0.5px; }
  .holder-role { font-family: "Source Sans 3", sans-serif; color: var(--ink-grey); font-size: 16px; margin-top: 8px; }
  .contacts {
    position: absolute; left: 44px; top: 284px;
    list-style: none;
    font-family: "Source Sans 3", sans-serif;
    font-size: 17px;
    color: var(--brand-blue);
  }
  .contacts li { display: flex; align-items: center; height: 23px; }
  .contacts svg { width: 14px; height: 14px; margin-right: 10px; fill: var(--brand-blue); }
  .card-back .wordmark { left: 396px; top: 260px; gap: 22px; }
  .card-back .wordmark-square { width: 108px; height: 108px; background: var(--brand-blue); }
  .card-back .wordmark-name { color: var(--brand-blue); font-size: 60px; }
</style>
</head>
<body>
  <section class="card card-front" aria-label="Card front">
    <div class="binary-field" role="img" aria-label="Faint binary digit pattern across the blue field"></div>
    <div class="wordmark">
      <span class="wordmark-square"></span>
      <span class="wordmark-name">KAV<br>REL</span>
    </div>
  </section>

  <section class="card card-back" aria-label="Card back">
    <svg class="header-wave" width="712" height="417" viewBox="0 0 712 417" aria-hidden="true">
      <path d="M0 58 C60 40 190 38 320 60 C470 90 560 175 712 185 V205 C560 198 470 110 320 82 C190 60 70 62 0 78 Z" fill="var(--swoosh-grey)"/>
      <path d="M0 0 H712 V180 C560 170 470 80 320 45 C190 18 60 22 0 36 Z" fill="var(--brand-blue)"/>
    </svg>
    <p class="company-name">KAVREL<br>s.r.o.</p>
    <div class="holder">
      <h1 class="holder-name">Lukáš Brezina</h1>
      <p class="holder-role">CEO</p>
    </div>
    <ul class="contacts">
      <li><svg viewBox="0 0 14 14"><path d="M1 4 C1 2 3 1 7 1 C11 1 13 2 13 4 L13 5 L10 5 L10 3.5 L4 3.5 L4 5 L1 5 Z M3 6 H11 L12 12 H2 Z"/></svg>www.kavrel.sk</li>
      <li><svg viewBox="0 0 14 14"><path d="M1 3 H13 V11 H1 Z M1.5 3.5 L7 8 L12.5 3.5" stroke="#fbfbfb" stroke-width="1"/></svg>+421 (0) 900 555 214</li>
      <li><svg viewBox="0 0 14 14"><circle cx="7" cy="7" r="6"/><path d="M1 7 H13 M7 1 C4 4 4 10 7 13 M7 1 C10 4 10 10 7 13" stroke="#fbfbfb" stroke-width="0.9" fill="none"/></svg>lukas.brezina@kavrel.sk</li>
      <li><svg viewBox="0 0 14 14"><path d="M7 0.5 C4 0.5 2 2.7 2 5.3 C2 8.8 7 13.5 7 13.5 C7 13.5 12 8.8 12 5.3 C12 2.7 10 0.5 7 0.5 Z M7 3.3 A2 2 0 1 0 7.01 3.3 Z" fill-rule="evenodd"/></svg>Lipová 12 811 01 Bratislava</li>
    </ul>
    <div class="wordmark">
      <span class="wordmark-square"></span>
      <span class="wordmark-name">KAV<br>REL</span>
    </div>
  </section>
</body>
</html>
```